Custom Cabinet Shop Needs a website design

Hi,
We need a website for a Custom Cabinet Shop and Cabinet parts manufacturing business.
The business has two sides to it. One side provides custom Kitchens, vanities, entertainment units, offices and what not to homeowners and contractors.
The 2nd side of the business provides built to order cabinet boxes and other parts required to put together a project to other cabinet shops, small contractors looking to install there own cabinets.
Website will need a Gallery to display work.
Color scheme to go well with logo.
current website is www.brindlewoodcustomcabinets.com
being changed to www.brindlewood.ca
Logo Included in attached files.
Tagline "Millwork with Flare"
Mission Statement "Our passion is to deliver inspired cabinetry solutions to suit all your needs, supported by our phenomenal star class customer service"
The website should convey quality and professionalism.
Thank you.
Homeowners/ Contractors
Entertainment
Coded - Design and coding required
1 page

```html
<!DOCTYPE html>
<html lang="en">
<head>
<meta charset="utf-8">
<title>Brindlewood Custom Cabinets</title>
<link rel="stylesheet" href="https://fonts.googleapis.com/css2?family=Raleway:wght@400;500;600&family=Muli:wght@400;600;700&display=swap">
<style>
  :root {
    --page-bg: #e6e6e6;
    --white: #ffffff;
    --ink: #1c1c1c;
    --muted: #555555;
    --orange: #f26522;
    --orange-light: #f47a3a;
    --panel: #ededed;
    --footer: #333333;
    --footer-deep: #2b2b2b;
    --footer-text: #a9a9a9;
    --footer-head: #f0f0f0;
  }
  * { box-sizing: border-box; margin: 0; padding: 0; }
  html, body { width: 1200px; height: 1176px; overflow: hidden; }
  body {
    position: relative;
    background: var(--page-bg);
    font-family: "Muli", Arial, sans-serif;
    color: var(--ink);
  }
  .side-photo {
    position: absolute; top: 110px; height: 414px;
    background: linear-gradient(180deg, #d9d9d9, #cfcfcf 60%, #dedede);
  }
  .side-photo.left { left: 0; width: 94px; }
  .side-photo.right { right: 0; width: 95px; }

  .page {
    position: absolute; left: 94px; top: 0; width: 1011px; height: 928px;
    background: var(--white);
    box-shadow: 0 0 8px rgba(0,0,0,.15);
  }

  /* header */
  .brand {
    position: absolute; left: 16px; top: 30px;
    display: flex; align-items: center; gap: 10px;
    font-family: "Raleway", sans-serif; font-weight: 600;
    font-size: 26px; color: var(--ink); letter-spacing: .5px;
  }
  .brand-dot { width: 34px; height: 34px; border-radius: 50%; background: var(--orange); }
  .phone {
    position: absolute; right: 77px; top: 22px;
    display: flex; align-items: center; gap: 12px;
    font-family: "Raleway", sans-serif; font-weight: 500; font-size: 25px; color: var(--ink);
  }
  .main-nav { position: absolute; left: 456px; top: 68px; display: flex; }
  .main-nav a {
    display: block; height: 37px; padding-top: 1px;
    font-family: "Raleway", sans-serif; font-weight: 600; font-size: 14px;
    color: var(--ink); text-decoration: none; text-align: center; position: relative;
  }
  .main-nav a.active::after {
    content: ""; position: absolute; left: 0; right: 0; bottom: 0; height: 4px; background: var(--orange);
  }
  .main-nav a.active::before {
    content: ""; position: absolute; left: 50%; bottom: 4px; margin-left: -5px;
    border: 5px solid transparent; border-bottom-color: var(--orange);
  }

  /* hero */
  .hero {
    position: absolute; left: 16px; top: 105px; width: 980px; height: 419px;
    background: radial-gradient(ellipse at 45% 45%, #4a4744 0%, #2f2c2a 55%, #1d1b1a 100%);
  }
  .hero-title {
    position: absolute; top: 172px; width: 100%; text-align: center;
    font-family: "Raleway", sans-serif; font-weight: 500; font-size: 41px; color: var(--white);
  }
  .hero-text {
    position: absolute; top: 229px; left: 220px; width: 540px; text-align: center;
    font-family: "Raleway", sans-serif; font-weight: 500; font-size: 14.5px; line-height: 18px; color: var(--white);
  }
  .hero-arrow {
    position: absolute; top: 196px; width: 45px; height: 45px; border-radius: 50%;
    background: #0a0a0a; display: flex; align-items: center; justify-content: center;
  }
  .hero-arrow.prev { left: 9px; }
  .hero-arrow.next { right: 9px; }

  /* tabs */
  .tabs {
    position: absolute; left: 16px; top: 561px; width: 980px; height: 39px;
    background: linear-gradient(180deg, #4a4a4a 0%, #111 45%, #000 100%);
    display: flex;
  }
  .tab {
    height: 39px; line-height: 39px; padding: 0 29px;
    font-family: "Raleway", sans-serif; font-size: 15px; color: var(--white);
    border-right: 1px solid #3a3a3a; position: relative;
  }
  .tab.active { background: var(--orange); width: 155px; text-align: center; padding: 0; border-right: none; }
  .tab.active::after {
    content: ""; position: absolute; left: 50%; margin-left: -7px; top: 39px;
    border: 7px solid transparent; border-top-color: var(--orange);
  }

  .gallery-panel { position: absolute; left: 16px; top: 600px; width: 980px; height: 328px; background: var(--panel); }
  .work-title { position: absolute; left: 17px; top: 40px; font-family: "Raleway", sans-serif; font-weight: 500; font-size: 22px; }
  .work-text { position: absolute; left: 18px; top: 77px; width: 195px; font-size: 13px; line-height: 20px; color: var(--muted); }
  .view-more { position: absolute; left: 21px; top: 194px; font-size: 13px; color: var(--orange); text-decoration: none; }
  .mini-nav { position: absolute; left: 20px; top: 235px; display: flex; gap: 2px; }
  .thumb {
    position: absolute; top: 42px; width: 232px; height: 217px;
    background: var(--white); padding: 6px; box-shadow: 0 1px 3px rgba(0,0,0,.3);
  }
  .thumb .photo { width: 100%; height: 100%; }
  .thumb.one { left: 235px; } .thumb.one .photo { background: linear-gradient(180deg, #bcb6ae, #4a4038 60%, #2e2925); }
  .thumb.two { left: 481px; } .thumb.two .photo { background: linear-gradient(180deg, #d8d4cc, #8a8077 55%, #3b3632); }
  .thumb.three { left: 726px; } .thumb.three .photo { background: linear-gradient(180deg, #4a3c33, #3a2f28 60%, #8a6a52); }

  /* footer */
  .site-footer { position: absolute; left: 0; top: 928px; width: 1200px; height: 193px; background: var(--footer); }
  .footer-brand {
    position: absolute; left: 112px; top: 80px; display: flex; align-items: center; gap: 10px;
    font-family: "Raleway", sans-serif; font-weight: 600; font-size: 24px; color: var(--white);
  }
  .footer-col { position: absolute; top: 27px; }
  .footer-col h3 { font-family: "Raleway", sans-serif; font-weight: 600; font-size: 14px; color: var(--footer-head); margin-bottom: 14px; }
  .footer-col li { list-style: none; font-size: 13px; line-height: 20px; color: var(--footer-text); }
  .topics { left: 398px; } .contact { left: 576px; } .contact li { font-size: 12.5px; }
  .newsletter { left: 834px; }
  .signup { display: flex; width: 253px; height: 34px; border: 1px solid #222; background: #2a2a2a; margin-top: 4px; }
  .signup span { flex: 1; line-height: 32px; padding-left: 8px; font-size: 11px; font-style: italic; color: #777; }
  .signup b { width: 82px; margin: 2px; background: #0d0d0d; color: var(--white); font-weight: 400; font-size: 13px; text-align: center; line-height: 28px; }
  .socials { position: absolute; left: 971px; top: 115px; display: flex; gap: 10px; }
  .socials span { width: 33px; height: 33px; background: #8c8c8c; border-radius: 2px; }
  .copyright {
    position: absolute; left: 0; top: 1121px; width: 1200px; height: 55px; background: var(--footer-deep);
    padding: 22px 0 0 108px; font-size: 12px; color: #9a9a9a;
  }
</style>
</head>
<body>
  <div class="side-photo left" role="img" aria-label="Faded photo of a white kitchen"></div>
  <div class="side-photo right" role="img" aria-label="Faded photo of a white vanity"></div>

  <div class="page">
    <header>
      <div class="brand"><span class="brand-dot"></span>BRINDLEWOOD</div>
      <div class="phone">
        <svg width="22" height="22" viewBox="0 0 24 24"><path fill="#1c1c1c" d="M6.6 10.8a15.1 15.1 0 0 0 6.6 6.6l2.2-2.2c.3-.3.7-.4 1-.2 1.1.4 2.3.6 3.6.6.6 0 1 .4 1 1V20c0 .6-.4 1-1 1A17 17 0 0 1 3 4c0-.6.4-1 1-1h3.5c.6 0 1 .4 1 1 0 1.3.2 2.5.6 3.6.1.3 0 .7-.2 1z"/></svg>
        403-555-0182
      </div>
      <nav class="main-nav">
        <a class="active" href="#" style="width:59px">Home</a>
        <a href="#" style="width:135px">Gallery</a>
        <a href="#" style="width:84px">Services</a>
        <a href="#" style="width:136px">Warranty</a>
        <a href="#" style="width:72px">Contact</a>
      </nav>
    </header>

    <section class="hero" role="img" aria-label="Dark wood kitchen with island, pendant lights and stainless fridge">
      <h1 class="hero-title">Millwork with Flare</h1>
      <p class="hero-text">Lorem ipsum dolor sit amet, consectetur adip iscing elit, sed do eiusmod incididuntut labore et doloreLorem ipsum dolor sit amet.</p>
      <span class="hero-arrow prev"><svg width="14" height="20" viewBox="0 0 14 20"><path d="M11 2 3 10l8 8" stroke="#fff" stroke-width="2.5" fill="none"/></svg></span>
      <span class="hero-arrow next"><svg width="14" height="20" viewBox="0 0 14 20"><path d="m3 2 8 8-8 8" stroke="#fff" stroke-width="2.5" fill="none"/></svg></span>
    </section>

    <div class="tabs">
      <div class="tab active">OUR GALLERY</div>
      <div class="tab">ABOUT US</div>
      <div class="tab">TESTIMONIALS</div>
    </div>

    <section class="gallery-panel">
      <h2 class="work-title">Our Work</h2>
      <p class="work-text">Lorem ipsum dolor sit amet, consectetur adipiscing elit, sed do eiusmod tempor incididunt ut labore et dolore magna aliqua. Ut enim ad minim</p>
      <a class="view-more" href="#">View More &gt;&gt;</a>
      <div class="mini-nav">
        <svg width="21" height="21" viewBox="0 0 21 21"><circle cx="10.5" cy="10.5" r="10" fill="#111"/><path d="M13 6v9l-6-4.5z" fill="#fff"/></svg>
        <svg width="21" height="21" viewBox="0 0 21 21"><circle cx="10.5" cy="10.5" r="10" fill="#111"/><path d="M8 6v9l6-4.5z" fill="#fff"/></svg>
      </div>
      <div class="thumb one"><div class="photo" role="img" aria-label="Wet bar with stone base and dark cabinets"></div></div>
      <div class="thumb two"><div class="photo" role="img" aria-label="Bright kitchen with island and pendant lights"></div></div>
      <div class="thumb three"><div class="photo" role="img" aria-label="Wall of dark flat-panel cabinets"></div></div>
    </section>
  </div>

  <footer class="site-footer">
    <div class="footer-brand"><span class="brand-dot"></span>BRINDLEWOOD</div>
    <div class="footer-col topics">
      <h3>Topic</h3>
      <ul><li>Advice</li><li>About</li><li>Contact</li><li>Privacy Policy</li><li>Terms &amp; Conditons</li></ul>
    </div>
    <div class="footer-col contact">
      <h3>Contact Info</h3>
      <ul><li>18420 Range Road 190</li><li>Cedar Ridge, Alberta</li><li>T1Z 0K4</li><li>Tel: 403-555-0182 or 403-555-0147</li><li>sales@brindlewoodcustomcabinets.com</li></ul>
    </div>
    <div class="footer-col newsletter">
      <h3>Join Our Newsletter</h3>
      <div class="signup"><span>Enter your email address</span><b>Subscribe</b></div>
    </div>
    <div class="socials"><span></span><span></span><span></span></div>
  </footer>
  <div class="copyright">Copyright © 2015 Brindlewood Custom Cabinets. Ltd. All rights reserved.</div>
</body>
</html>
```